Brevinor
Brevinor - Consulting
Use same font as used in my logo
It is up to you.
Simple
Lionel Brasquet
President
82 Thornwell Avenue Toronto, Ontario M4R 2J8
l.brasquet@brevinorhub.com
www.brevinorhub.com
Will be the same however in French

```html
<!DOCTYPE html>
<html lang="en">
<head>
<meta charset="utf-8">
<title>Brevinor – Stationery</title>
<link rel="stylesheet" href="https://fonts.googleapis.com/css2?family=Michroma&family=Open+Sans:wght@400;600&display=swap">
<style>
  :root {
    --bg: #ece8e2;
    --paper: #ffffff;
    --paper-edge: #dcdcdc;
    --band-dark: #0e151c;
    --band-mid: #2b3a48;
    --band-light: #3d5163;
    --logo: #ffffff;
    --logo-dark: #1d2a36;
    --text: #6a6f75;
    --text-light: #c9d1d8;
    --flap-blue: #1f4a7a;
    --flap-blue-light: #3568a0;
    --flap-grey: #7d7f82;
    --flap-grey-light: #a3a5a8;
    --flap-white: #f4f4f4;
    --caption: #8a8178;
  }
  * { box-sizing: border-box; margin: 0; padding: 0; }
  html, body { width: 1200px; height: 600px; overflow: hidden; }
  body {
    background: var(--bg);
    position: relative;
    font-family: "Open Sans", Arial, sans-serif;
    color: var(--text);
  }
  .band {
    background:
      radial-gradient(ellipse at 30% 40%, var(--band-light) 0%, transparent 60%),
      linear-gradient(90deg, var(--band-dark) 0%, var(--band-mid) 45%, var(--band-dark) 100%);
    color: var(--text-light);
  }
  .brand {
    font-family: "Michroma", "Arial Black", sans-serif;
    color: var(--logo);
    letter-spacing: 0.04em;
    display: flex;
    align-items: center;
    gap: 0.45em;
    white-space: nowrap;
  }
  .brand .dot {
    width: 0.55em; height: 0.55em;
    border-radius: 50%;
    background: currentColor;
    display: inline-block;
  }
  .brand--dark { color: var(--logo-dark); }
  .sheet {
    position: absolute;
    background: var(--paper);
    box-shadow: 0 2px 6px rgba(0,0,0,0.18);
  }

  /* business cards */
  .card-front { left: 29px; top: 180px; width: 125px; height: 67px; overflow: hidden; }
  .card-front .band { height: 24px; display: flex; align-items: center; padding-left: 10px; }
  .card-front .brand { font-size: 7px; }
  .card-front .details { display: flex; justify-content: space-between; padding: 7px 8px; font-size: 3.4px; line-height: 1.45; }
  .card-front .person strong { display: block; font-weight: 600; color: #33383d; }
  .card-back { left: 29px; top: 300px; width: 125px; height: 80px; display: flex; align-items: center; justify-content: center; border-bottom: 5px solid var(--band-dark); }
  .card-back .brand { font-size: 8px; }

  /* letterhead */
  .letterhead { left: 221px; top: 24px; width: 403px; height: 528px; }
  .letterhead .band { height: 60px; display: flex; align-items: center; justify-content: space-between; padding: 0 22px 0 26px; }
  .letterhead .brand { font-size: 17px; }
  .letterhead .contact { display: flex; gap: 14px; font-size: 5px; line-height: 1.5; }

  /* envelopes */
  .envelope-back { position: absolute; filter: drop-shadow(0 2px 3px rgba(0,0,0,0.18)); }
  .env-blue { left: 720px; top: 24px; }
  .env-grey { left: 684px; top: 132px; }
  .env-white { left: 720px; top: 236px; }
  .envelope-front { left: 653px; top: 355px; width: 439px; height: 192px; }
  .envelope-front .band { height: 60px; display: flex; align-items: center; padding-left: 28px; }
  .envelope-front .brand { font-size: 16px; }
  .envelope-front .return { padding: 14px 28px; font-size: 5px; line-height: 1.6; }

  .caption {
    position: absolute; top: 568px;
    font-family: "Open Sans", Arial, sans-serif;
    font-size: 8px; letter-spacing: 0.12em; color: var(--caption);
    font-variant: small-caps;
  }
  .caption--letterhead { left: 372px; }
  .caption--envelope { left: 820px; }
</style>
</head>
<body>

  <section class="sheet card-front" aria-label="Business card front">
    <div class="band"><span class="brand"><span class="dot"></span>BREVINOR</span></div>
    <div class="details">
      <p class="person"><strong>Lionel Brasquet</strong>President</p>
      <p class="address">82 Thornwell Avenue<br>Toronto, Ontario M4R 2J8<br>l.brasquet@brevinorhub.com<br>www.brevinorhub.com</p>
    </div>
  </section>

  <section class="sheet card-back" aria-label="Business card back">
    <span class="brand brand--dark"><span class="dot"></span>BREVINOR</span>
  </section>

  <section class="sheet letterhead" aria-label="Letterhead">
    <header class="band">
      <span class="brand"><span class="dot"></span>BREVINOR</span>
      <div class="contact">
        <p>82 Thornwell Avenue<br>Toronto, Ontario M4R 2J8</p>
        <p>l.brasquet@brevinorhub.com<br>www.brevinorhub.com</p>
      </div>
    </header>
  </section>

  <svg class="envelope-back env-blue" width="372" height="190" viewBox="0 0 372 190" aria-label="Envelope with blue flap">
    <defs>
      <linearGradient id="flapBlue" x1="0" y1="0" x2="0" y2="1">
        <stop offset="0" stop-color="var(--flap-blue-light)"/>
        <stop offset="1" stop-color="var(--flap-blue)"/>
      </linearGradient>
    </defs>
    <rect x="0" y="0" width="372" height="190" fill="var(--paper)"/>
    <path d="M0 0 H372 V62 Q372 78 356 80 H16 Q0 78 0 62 Z" fill="url(#flapBlue)"/>
  </svg>

  <svg class="envelope-back env-grey" width="408" height="180" viewBox="0 0 408 180" aria-label="Envelope with grey flap">
    <defs>
      <linearGradient id="flapGrey" x1="0" y1="0" x2="0" y2="1">
        <stop offset="0" stop-color="var(--flap-grey-light)"/>
        <stop offset="1" stop-color="var(--flap-grey)"/>
      </linearGradient>
    </defs>
    <rect x="0" y="0" width="408" height="180" fill="var(--paper)"/>
    <path d="M0 0 H408 V66 Q408 86 388 88 H20 Q0 86 0 66 Z" fill="url(#flapGrey)"/>
  </svg>

  <svg class="envelope-back env-white" width="372" height="100" viewBox="0 0 372 100" aria-label="Envelope with white flap">
    <rect x="0" y="0" width="372" height="100" fill="var(--paper)"/>
    <path d="M0 0 H372 V52 Q372 66 358 68 H14 Q0 66 0 52 Z" fill="var(--flap-white)" stroke="var(--paper-edge)" stroke-width="1"/>
  </svg>

  <section class="sheet envelope-front" aria-label="Envelope front">
    <div class="band"><span class="brand"><span class="dot"></span>BREVINOR</span></div>
    <p class="return">82 Thornwell Avenue<br>Toronto, Ontario M4R 2J8</p>
  </section>

  <p class="caption caption--letterhead">Letter-head Option 1</p>
  <p class="caption caption--envelope">Envelope Option 2</p>

</body>
</html>
```